Chiropractic Flyers to be made more up to date

I have used this series of flyers for my own practice. I would like the graphics to be brought up to date and the name of the doctor and the practice, the address, phone number and date to be removed and a blank box inserted in one place on the flyer that other chiropractors could use to personalize the flyers for their practice. On some of the flyers, this information is in several places. I'd like to have it all in one space so that it would be easy for the doctor to add it in their practice. They all need to be bright and colorful with catchy graphics.

```html
<!DOCTYPE html>
<html lang="en">
<head>
<meta charset="utf-8">
<title>Backpack Safety Demonstration</title>
<link rel="stylesheet" href="https://fonts.googleapis.com/css2?family=Rye&family=Tinos&display=swap">
<style>
  :root {
    --paper: #f7f4de;
    --paper-light: #fbfaf0;
    --ray: #f3ecc0;
    --ink: #2b2b2b;
    --border-band: #ebe1ac;
    --pack-red: #b83a3e;
    --pack-red-dark: #8e2a2e;
    --pack-blue: #3f3a8f;
    --pack-blue-dark: #2a2666;
    --burst-fill: #ffffff;
    --burst-shadow: #2e2e2e;
    --ribbon: #e9e9e9;
    --ribbon-fold: #bdbdbd;
  }
  * { box-sizing: border-box; margin: 0; padding: 0; }
  html, body { width: 900px; height: 1200px; overflow: hidden; background: #ffffff; }

  .flyer {
    position: relative;
    width: 900px;
    height: 1200px;
    overflow: hidden;
    background:
      radial-gradient(circle at 50% 45%, var(--paper-light) 0%, var(--paper) 55%, var(--ray) 100%);
    color: var(--ink);
  }

  .pencil-border {
    position: absolute;
    left: 22px; top: 26px; right: 22px; bottom: 26px;
    border: 42px solid var(--border-band);
    opacity: 0.75;
  }

  .title {
    position: absolute;
    left: 0; right: 0; top: 100px;
    text-align: center;
    font-family: "Rye", serif;
    font-weight: 400;
    line-height: 1;
    color: var(--ink);
  }
  .title__line { display: block; }
  .title__line--big { font-size: 62px; letter-spacing: 10px; margin-bottom: 18px; }
  .title__line--wide { font-size: 47px; letter-spacing: 6px; }

  .pack {
    position: absolute;
    border-radius: 40px 40px 18px 18px;
  }
  .pack--red {
    left: 120px; top: 362px; width: 220px; height: 246px;
    background: linear-gradient(160deg, var(--pack-red) 0%, var(--pack-red-dark) 100%);
  }
  .pack--blue {
    left: 612px; top: 890px; width: 190px; height: 205px;
    background: linear-gradient(160deg, var(--pack-blue) 0%, var(--pack-blue-dark) 100%);
  }

  .burst {
    position: absolute;
    left: 405px; top: 378px;
    width: 385px; height: 225px;
  }
  .burst__text {
    position: absolute;
    left: 0; right: 0; top: 80px;
    text-align: center;
    font-family: "Rye", serif;
    color: var(--ink);
    line-height: 1;
  }
  .burst__line--top { display: block; font-size: 27px; letter-spacing: 3px; }
  .burst__line--bottom { display: block; font-size: 18px; letter-spacing: 2px; margin-top: 4px; }

  .points {
    position: absolute;
    left: 70px; top: 645px; width: 760px;
    list-style: none;
    font-family: "Tinos", serif;
    font-size: 27px;
    line-height: 36px;
    color: var(--ink);
  }
  .points li {
    position: relative;
    padding-left: 28px;
    margin-bottom: 3px;
  }
  .points li::before {
    content: "";
    position: absolute;
    left: 4px; top: 15px;
    width: 7px; height: 7px;
    background: var(--ink);
    transform: rotate(45deg);
  }

  .invite {
    position: absolute;
    left: 67px; top: 875px; width: 550px; height: 50px;
    border-top: 1.5px solid var(--ink);
    border-bottom: 1.5px solid var(--ink);
    font-family: "Rye", serif;
    font-size: 19px;
    letter-spacing: 3px;
    line-height: 47px;
    color: var(--ink);
  }

  .practice-box {
    position: absolute;
    left: 76px; top: 950px;
    width: 505px; height: 168px;
  }
</style>
</head>
<body>
  <main class="flyer">
    <div class="pencil-border" role="img" aria-label="Border of small yellow pencils around the flyer"></div>

    <h1 class="title">
      <span class="title__line title__line--big">BACKPACK</span>
      <span class="title__line title__line--big">SAFETY</span>
      <span class="title__line title__line--wide">DEMONSTRATION</span>
    </h1>

    <div class="pack pack--red" role="img" aria-label="Illustration of a red school backpack with a yellow front pocket"></div>

    <div class="burst">
      <svg width="385" height="225" viewBox="0 0 385 225" aria-hidden="true">
        <polygon fill="var(--burst-shadow)" transform="translate(12,10)"
          points="192,4 214,40 252,10 258,52 310,28 296,70 360,62 322,100 378,118 322,132 352,172 296,162 300,208 256,180 238,220 210,184 182,222 164,184 126,216 120,176 68,200 80,158 18,166 56,128 6,112 58,96 22,58 84,70 74,26 126,52 140,10 168,44"/>
        <polygon fill="var(--burst-fill)" stroke="var(--burst-shadow)" stroke-width="1.5"
          points="192,4 214,40 252,10 258,52 310,28 296,70 360,62 322,100 378,118 322,132 352,172 296,162 300,208 256,180 238,220 210,184 182,222 164,184 126,216 120,176 68,200 80,158 18,166 56,128 6,112 58,96 22,58 84,70 74,26 126,52 140,10 168,44"/>
      </svg>
      <p class="burst__text">
        <span class="burst__line--top">STAND UP</span>
        <span class="burst__line--bottom">FOR SUCCESS</span>
      </p>
    </div>

    <ul class="points">
      <li>Learn how your posture can effect your attitude and self-esteem</li>
      <li>Learn the posture of a “Winner” &amp; how to avoid the posture of a “Loser”.</li>
      <li>Learn proper backpack safety to stand up for success</li>
    </ul>

    <p class="invite">PARENTS &amp; FACULTY INVITED</p>

    <svg class="practice-box" viewBox="0 0 505 168" aria-label="Blank space for practice details">
      <polygon fill="var(--ribbon-fold)" points="10,110 40,110 40,160 0,168"/>
      <polygon fill="var(--ribbon-fold)" points="465,110 495,110 505,168 465,160"/>
      <polygon fill="var(--ribbon)" points="0,4 505,0 490,130 12,134"/>
    </svg>

    <div class="pack pack--blue" role="img" aria-label="Illustration of a blue school backpack"></div>
  </main>
</body>
</html>
```